Attorney Website Design

I need a top quality attorney website layout designed. Here are some examples of what I feel are great websites:
http://www.quellmarstonseparationlaw.com/
http://www.vandriclegalgroup.com/
http://www.pobelaw.com/
http://www.harrowvaleaccusedcounselhq.com/
http://www.tzlegal.com/
http://www.brookhollowtrialjusticeoffice.com/
http://www.orvynchargedcounsel.com/
http://www.tzlegal.com/
What we like about these sites:
• The different layers
• Subtle designs, textures, curves
• 3 dimensional
• Floating effects
• Prominent phone number
• Location of Areas of Practice
• Request A Consultation Prominent
• Right side bar with practice areas
• Badges
• Clear Calls to Action
• Dynamic/Staying Top navigation when you scroll
The project will be for a home page and then also an interior page (should be similar to home page).
Updates
I want to make it understood I am looking for a design which is not a typical "template" site which I can find anywhere for $50. This budget and project is for a "Custom" website design. Please submit designs similar in quality to the samples links I have posted. Creativity is a MUST! The best way to explain this is, I want a design that I can feel it unique and original, not something that looks like 95% of all websites out there.
Neil
I just wanted everyone to know that so far I am not to pleased with any of the designs. I am not looking for cut/pasting of other peoples websites but ORIGINAL and CREATIVE work.
Reason: Weekend + Holiday extension.
Reason: Need more designs
Industry/Entity Type
Attorney

```html
<!DOCTYPE html>
<html lang="en">
<head>
<meta charset="utf-8">
<title>Brookhollow Attorneys</title>
<link href="https://fonts.googleapis.com/css2?family=Cinzel:wght@400;600&family=Oswald:wght@700&family=Arimo:wght@400;700&family=Open+Sans:wght@400;600&family=Libre+Baskerville:ital@1&display=swap" rel="stylesheet">
<style>
:root{
  --ink:#111;
  --header:#161616;
  --orange:#f47c0b;
  --orange-dark:#d86a05;
  --wood:#b9631e;
  --wood-dark:#a55518;
  --panel:#e4e4e4;
  --white:#fff;
  --rule:#d4d4d4;
  --text:#2b2b2b;
  --muted:#7a7a7a;
  --brown:#8e4a12;
}
*{box-sizing:border-box;margin:0;padding:0}
html,body{width:913px;height:1200px;overflow:hidden}
body{position:relative;background:linear-gradient(180deg,var(--wood),var(--wood-dark));font-family:Arimo,Arial,sans-serif;color:var(--text)}
.abs{position:absolute}
.site-header{left:0;top:0;width:913px;height:82px;background:radial-gradient(ellipse at 50% 0,#2e2e2e,var(--header) 70%)}
.brand{left:0;width:913px;top:0;height:82px;line-height:82px;text-align:center;color:#f2f2f2;font-family:Arimo,Arial,sans-serif;font-weight:400;font-size:26px}
.main-nav{left:0;top:82px;width:913px;height:36px;background:linear-gradient(180deg,#ff8a17,var(--orange-dark));border-bottom:1px solid #9c4c08}
.nav-item{top:0;height:36px;line-height:36px;font-size:9px;color:#fff;font-family:Arimo,sans-serif}
.nav-item.active{top:9px;height:20px;line-height:18px;border:1px solid #5a2a00;border-radius:2px;width:50px;text-align:center;left:112px}
.nav-sep{top:9px;width:1px;height:19px;background:rgba(255,255,255,.35)}
.cta{left:650px;top:90px;width:156px;height:21px;border:1px solid #3a1a00;border-radius:2px;color:#fff;font-size:8px;font-weight:700;line-height:19px;padding-left:25px}
.cta svg{position:absolute;left:7px;top:5px}
.hero{left:95px;top:126px;width:722px;height:313px;background:linear-gradient(180deg,#5a3e2a 0%,#3a2a20 40%,#1d1712 100%)}
.arrow{top:252px}
.hero-title{left:170px;top:306px;font-family:Oswald,sans-serif;font-size:34px;line-height:36px;color:#fff;letter-spacing:.3px}
.hero-text{left:170px;top:345px;width:340px;font-size:10.5px;line-height:16px;color:#fff}
.side-panel{left:95px;top:439px;width:722px;height:677px;background:var(--panel)}
.content{left:125px;top:416px;width:662px;height:700px;background:var(--white)}
.consult{left:125px;top:416px;width:662px;height:80px;background:linear-gradient(180deg,#ececec,#fff)}
.section-title{font-family:Cinzel,serif;font-weight:600}
.consult-title{left:139px;top:428px;font-size:19px;color:var(--orange)}
.field{top:463px;height:26px;border:1px solid #b7b7b7;border-radius:2px;background:#fff;font-size:9px;color:#555;line-height:24px;padding-left:7px}
.submit{left:720px;top:464px;width:52px;height:24px;background:linear-gradient(180deg,#a55a1a,var(--brown));color:#fff;font-weight:700;font-size:10px;line-height:24px;text-align:center}
.rule{height:1px;background:var(--rule)}
.quote{left:150px;top:535px;width:615px;font-family:"Libre Baskerville",serif;font-style:italic;font-size:18px;line-height:30px;letter-spacing:.5px;color:#222}
.quote .mark{font-family:Georgia,serif;color:#bdbdbd;font-size:26px;font-style:normal}
.helping-title{left:141px;top:648px;font-size:21px;color:#111}
.helping-text{left:141px;top:688px;width:310px;font-size:10px;line-height:12.7px;color:#222}
.helping-text p+p{margin-top:12.7px}
.video{left:465px;top:646px;width:295px;height:172px;background:linear-gradient(135deg,#3d4a55,#1e2630 60%,#111);border:2px solid #222}
.video-bar{left:465px;top:788px;width:295px;height:30px;background:#141414}
.col-title{top:874px;font-family:"Open Sans",sans-serif;font-size:15px;font-weight:400;color:#222}
.small{font-family:"Open Sans",sans-serif;font-size:8.5px;line-height:16px;color:#333}
.news-title{left:139px;top:906px;font-family:"Open Sans",sans-serif;font-size:12px;font-weight:600;color:#333}
.news-date{left:139px;top:925px;font-family:"Open Sans",sans-serif;font-size:8.5px;color:var(--muted)}
.more{left:139px;top:1040px;font-family:"Open Sans",sans-serif;font-size:9px;color:#666;letter-spacing:.3px}
.tweets{left:355px;top:910px;width:191px;height:153px;border:1px solid #ddd;background:#fff}
.tweet{left:12px;width:168px;font-family:"Open Sans",sans-serif;font-size:8px;line-height:14px;color:#333}
.tweet .ago{display:block;margin-top:3px;font-size:7px;color:#888}
.testimonial{left:574px;top:910px;width:200px;height:124px;border:1px solid #ddd;background:#fff;padding:12px 12px}
.author{left:574px;top:1050px;width:201px;text-align:right;font-family:"Open Sans",sans-serif;font-size:8.5px;color:#222}
.author b{font-weight:600}
.author em{font-style:normal;color:var(--orange)}
.skyline{left:320px;top:1094px;width:288px;height:22px;background:linear-gradient(180deg,rgba(17,17,17,0),#111)}
.site-footer{left:0;top:1116px;width:913px;height:84px;background:#0c0c0c}
.foot-links{left:113px;top:1146px;font-size:8.5px;color:#eee}
.copy{left:113px;top:1170px;font-size:8.5px;color:#eee}
.social{top:1153px;width:24px;height:24px;border-radius:50%;background:radial-gradient(circle at 40% 35%,#d8d8d8,#8d8d8d);border:1px solid #444}
.newsletter{left:606px;top:1153px;width:170px;height:22px;background:#fff;font-size:8px;color:#666;line-height:22px;padding-left:6px}
.go{left:776px;top:1153px;width:25px;height:22px;background:var(--orange);color:#fff;font-size:10px;font-weight:700;line-height:22px;text-align:center}
</style>
</head>
<body>

<header class="abs site-header">
  <div class="abs brand">Brookhollow Attorneys</div>
</header>

<nav class="abs main-nav">
  <span class="abs nav-item active" style="top:8px">HOME</span>
  <span class="abs nav-sep" style="left:169px"></span>
  <span class="abs nav-item" style="left:183px">OUR FIRM</span>
  <span class="abs nav-sep" style="left:240px"></span>
  <span class="abs nav-item" style="left:258px">PRACTICE &nbsp;AREAS</span>
  <span class="abs nav-sep" style="left:346px"></span>
  <span class="abs nav-item" style="left:363px">ATTORNEYS</span>
  <span class="abs nav-sep" style="left:430px"></span>
  <span class="abs nav-item" style="left:446px">TESTIMONIALS</span>
  <span class="abs nav-sep" style="left:523px"></span>
  <span class="abs nav-item" style="left:541px">CONTACT US</span>
</nav>
<a class="abs cta" style="top:90px">
  <svg width="12" height="9" viewBox="0 0 12 9"><rect x=".5" y=".5" width="11" height="8" fill="#111" stroke="#111"/><path d="M1 1l5 4 5-4" fill="none" stroke="#f47c0b" stroke-width="1"/></svg>
  REQUEST FREE CONSULTATION
</a>

<div class="abs side-panel"></div>

<section class="abs hero" role="img" aria-label="Group photo of the firm's attorneys standing in a law library"></section>
<svg class="abs arrow" style="left:110px" width="18" height="30" viewBox="0 0 18 30"><path d="M15 2L3 15l12 13" fill="none" stroke="#fff" stroke-width="4"/></svg>
<svg class="abs arrow" style="left:786px" width="18" height="30" viewBox="0 0 18 30"><path d="M3 2l12 13L3 28" fill="none" stroke="#fff" stroke-width="4"/></svg>
<h1 class="abs hero-title">ATTORNEYS YOU CAN TRUST</h1>
<p class="abs hero-text">simply dummy text of the printing and typesetting industry. Lorem Ipsum has been the industry's standard dummy text ever since the 1500s,</p>

<main>
  <div class="abs content"></div>
  <div class="abs consult"></div>
  <h2 class="abs section-title consult-title">Request Free Consultation</h2>
  <div class="abs field" style="left:139px;width:119px">NAME</div>
  <div class="abs field" style="left:266px;width:119px">EMAIL</div>
  <div class="abs field" style="left:394px;width:118px">PHONE</div>
  <div class="abs field" style="left:521px;width:252px">DESCRIBE YOUR CASE</div>
  <div class="abs submit">SUBMIT</div>

  <div class="abs rule" style="left:141px;top:511px;width:629px"></div>
  <blockquote class="abs quote"><span class="mark">&ldquo;</span> We guide you through this often complex and confusing legal process, allowing you time to heal and recuperate. <span class="mark">&rdquo;</span></blockquote>
  <div class="abs rule" style="left:141px;top:615px;width:629px"></div>

  <h2 class="abs section-title helping-title">Who We're Helping Now</h2>
  <div class="abs helping-text">
    <p>For family-owned or privately-held businesses, acquisitions transactions offer opportunities for market expansion, growth or streamlining of the business. We can help you develop an acquisition strategy, identify target organizations and strategic partners, determine the appropriate bid price,</p>
    <p>Perform financial and tax due diligence reviews, perform a risk assessment, assess the timing of the sale...</p>
  </div>
  <div class="abs video" role="img" aria-label="Video still of two professionals in conversation"></div>
  <svg class="abs" style="left:585px;top:693px" width="56" height="56" viewBox="0 0 56 56"><circle cx="28" cy="28" r="25" fill="rgba(0,0,0,.35)" stroke="#fff" stroke-width="3"/><path d="M22 17l16 11-16 11z" fill="#fff"/></svg>
  <div class="abs video-bar"></div>
  <svg class="abs" style="left:473px;top:796px" width="280" height="14" viewBox="0 0 280 14">
    <path d="M2 2l8 5-8 5z" fill="#fff"/>
    <rect x="20" y="6" width="212" height="2" fill="#ddd"/><rect x="20" y="6" width="94" height="2" fill="#f47c0b"/>
    <path d="M243 5h3l4-3v10l-4-3h-3z" fill="#fff"/><path d="M252 4q3 3 0 6" stroke="#fff" fill="none"/>
    <rect x="265" y="2" width="11" height="10" fill="none" stroke="#fff" stroke-width="1.5"/>
  </svg>

  <div class="abs rule" style="left:137px;top:843px;width:629px"></div>

  <h3 class="abs col-title" style="left:139px">Latest News</h3>
  <div class="abs news-title">Lorem ipsum dolor sit amet</div>
  <div class="abs news-date">14<sup style="font-size:6px">th</sup> November</div>
  <p class="abs small" style="left:139px;top:949px;width:200px">Nam libero tempore, cum soluta nobis est eligendi optio cumque nihil impedit quo lorem ipsum dolor sit &nbsp;minus id quod maxime placeat facere possimus, omnis voluptas assumenda est, omnis dolor repellendus...</p>
  <div class="abs more">FULL ARTICLE &nbsp;&rsaquo;</div>

  <h3 class="abs col-title" style="left:357px">Recent Tweets</h3>
  <div class="abs tweets">
    <div class="abs tweet" style="top:10px"><span style="color:#777">@ledgerline</span> Lorem ipsum dolor sit amet consectetur adipisicing elit.<span class="ago">9 hours ago</span></div>
    <div class="abs rule" style="left:0;top:69px;width:189px"></div>
    <div class="abs tweet" style="top:79px"><span style="color:#777">@northquill</span> At vero eos et accusamus et iusto odio dignissimos ducimus blanditiis praesentium voluptatum<span class="ago">1 day ago</span></div>
  </div>

  <h3 class="abs col-title" style="left:574px">Our Client's are Awesome</h3>
  <svg class="abs" style="left:749px;top:897px" width="20" height="6" viewBox="0 0 20 6"><circle cx="3" cy="3" r="1.6" fill="#ccc"/><circle cx="9" cy="3" r="1.6" fill="#ccc"/><circle cx="15" cy="3" r="1.8" fill="#777"/></svg>
  <div class="abs testimonial"><p class="small" style="line-height:16px">At vero eos et accusamus et lucero iusto od dignissimos ducimus qui blanditiis praesen voluptatum deleniti atque corrupti quos do et quas molestias excepturi sint occaecati cupiditate non provident.</p><span class="abs" style="right:10px;bottom:0;font-family:Georgia,serif;font-size:22px;color:#333">&rdquo;</span></div>
  <div class="abs author"><b>John Doe</b>, <em>xyz etc.</em>, cat lover</div>

  <div class="abs skyline" role="img" aria-label="City skyline silhouette"></div>
</main>

<footer class="abs site-footer"></footer>
<div class="abs foot-links">O NAS | INDYWIDUALNI | KORPORACYJNI | KONTAKT</div>
<div class="abs copy">&copy; 2014 &nbsp;Brookhollow Law, All Rights Reserved</div>
<span class="abs social" style="left:391px"></span>
<span class="abs social" style="left:423px"></span>
<span class="abs social" style="left:455px"></span>
<span class="abs social" style="left:488px"></span>
<span class="abs social" style="left:520px"></span>
<div class="abs newsletter">Sign up to our newsletter</div>
<div class="abs go">GO</div>

</body>
</html>
```